New Business Card Design Project

Make a kick ass business card for The Otter Tea Mug, using the designs. I also might like the 2nd place design logo on the back? Maybe all black with that? Not sure. Also, I'm cool with it being on metal, plastic, glass? or whatever for the business card. Maybe shaped like a shark? Let me know what else you need? Would like designs in the next day or so. Thank you.
Target Market(s)
Anyone that is cool
Contact Information for Business Card
Name: Dorian Fenwick
Phone: 317.594.8126
inventor/creator/entrepreneur/owner
www.theottertyeamug.example
social media links
https://www.facebook.com/theottertyeamug
https://twitter.com/otter_brew
https://www.instagram.com/theottertyeamug/
I'll get the Pinterest one soon
Colors
Designer to choose colors to be used in the design.
Requirements
Must have
- The Otter Tea Mug
- www.theottertyeamug.example
- social media tags?
- My logos and picture/photo of wine glass
Nice to have
- Maybe shaped like a wine glass or shark
- I'll let you decide but my same colors from my website would be nice

```html
<!DOCTYPE html>
<html lang="en">
<head>
<meta charset="utf-8">
<title>The Otter Tea Mug – Business Card</title>
<link href="https://fonts.googleapis.com/css2?family=Josefin+Sans:wght@300;400;700&display=swap" rel="stylesheet">
<style>
  :root {
    --backdrop: #34363a;
    --card-white: #ffffff;
    --brand-red: #c2434b;
    --brand-red-dark: #a8353c;
    --swoosh-grey: #8e8f93;
    --text-grey: #6f7074;
    --divider: #8a8b8f;
    --metal-light: #a9aaae;
    --metal-dark: #6f7074;
    --metal-text: #45464a;
  }
  * { box-sizing: border-box; margin: 0; padding: 0; }
  html, body {
    width: 1200px; height: 900px; overflow: hidden;
    background: var(--backdrop);
    font-family: "Josefin Sans", sans-serif;
  }
  .stage { position: relative; width: 1200px; height: 900px; }

  .card {
    position: absolute; width: 700px; height: 400px;
    box-shadow: 0 10px 28px rgba(0,0,0,.45);
    overflow: hidden;
  }

  /* Front: metallic grey */
  .card-front {
    left: 160px; top: 50px;
    background: linear-gradient(135deg, var(--metal-dark) 0%, var(--metal-light) 45%, var(--metal-dark) 100%);
    display: flex; align-items: center; justify-content: center;
  }
  .front-wordmark {
    display: flex; align-items: center; gap: 16px;
    font-weight: 300; font-size: 50px; color: var(--metal-text);
    letter-spacing: .5px;
  }
  .front-wordmark .mark-dot {
    width: 26px; height: 26px; border-radius: 50%; background: var(--metal-text);
  }

  /* Back: white with red wave */
  .card-back {
    left: 340px; top: 440px;
    background: var(--card-white);
  }
  .wave { position: absolute; inset: 0; width: 700px; height: 400px; }

  .brand-block {
    position: absolute; left: 40px; top: 150px; width: 310px;
    display: flex; align-items: center; gap: 12px;
  }
  .brand-name {
    font-weight: 400; font-size: 30px; color: var(--brand-red);
    white-space: nowrap;
  }
  .brand-block .mark-dot {
    width: 18px; height: 18px; border-radius: 50%; background: var(--brand-red); flex: none;
  }

  .divider {
    position: absolute; left: 380px; top: 40px; width: 1px; height: 230px;
    background: var(--divider);
  }

  .contact {
    position: absolute; left: 400px; top: 46px; width: 290px;
    color: var(--text-grey);
  }
  .person-name { font-weight: 700; font-size: 22px; color: var(--brand-red); }
  .person-title { font-weight: 300; font-size: 13.5px; margin-top: 4px; }
  .lines { list-style: none; margin-top: 12px; }
  .lines li {
    display: flex; align-items: center; gap: 8px;
    font-weight: 300; font-size: 14px; line-height: 20px;
  }
  .lines .gap { margin-top: 10px; }
  .lines svg { width: 12px; height: 12px; flex: none; }
  .social-square {
    width: 11px; height: 11px; border-radius: 2px; flex: none;
    background: var(--brand-red);
  }
</style>
</head>
<body>
<main class="stage">
  <section class="card card-front" aria-label="Card front">
    <div class="front-wordmark">
      <span class="mark-dot" aria-hidden="true"></span>
      <span>The Otter Tea Mug</span>
    </div>
  </section>

  <section class="card card-back" aria-label="Card back">
    <svg class="wave" viewBox="0 0 700 400" aria-hidden="true">
      <path d="M0 365 C 220 352 470 300 700 175 L700 400 L0 400 Z" fill="var(--brand-red)"/>
      <path d="M0 352 C 230 338 470 290 690 178" fill="none" stroke="var(--card-white)" stroke-width="10"/>
      <path d="M0 343 C 230 330 460 286 680 178" fill="none" stroke="var(--swoosh-grey)" stroke-width="7"/>
    </svg>

    <div class="brand-block">
      <span class="mark-dot" aria-hidden="true"></span>
      <span class="brand-name">The Otter Tea Mug</span>
    </div>

    <div class="divider" aria-hidden="true"></div>

    <div class="contact">
      <h1 class="person-name">Dorian Fenwick</h1>
      <p class="person-title">inventor/creator/entrepreneur/owner</p>
      <ul class="lines">
        <li>
          <svg viewBox="0 0 12 12"><path d="M2.5 1 L4.5 1 L5.3 3.4 L4 4.4 C4.6 5.8 6.2 7.4 7.6 8 L8.6 6.7 L11 7.5 L11 9.5 C11 10.3 10.3 11 9.5 11 C5 11 1 7 1 2.5 C1 1.7 1.7 1 2.5 1 Z" fill="none" stroke="var(--brand-red)" stroke-width="1"/></svg>
          317.594.8126
        </li>
        <li>
          <svg viewBox="0 0 12 12"><circle cx="6" cy="6" r="5" fill="none" stroke="var(--brand-red)" stroke-width="1"/><ellipse cx="6" cy="6" rx="2.2" ry="5" fill="none" stroke="var(--brand-red)" stroke-width="1"/><line x1="1" y1="6" x2="11" y2="6" stroke="var(--brand-red)" stroke-width="1"/></svg>
          www.theottertyeamug
        </li>
        <li class="gap"><span class="social-square" aria-hidden="true"></span>theottertyeamug</li>
        <li><span class="social-square" aria-hidden="true"></span>otter_brew</li>
        <li><span class="social-square" aria-hidden="true"></span>theottertyeamug</li>
        <li><span class="social-square" aria-hidden="true"></span>theottertyeamug</li>
      </ul>
    </div>
  </section>
</main>
</body>
</html>
```